Verpackungsdesign für Schokoladen Geschenkboxen
Zielgruppe
Wir machen Schokolade und suchen für unsere 3 er Geschenkboxen mit Fenster, deren äußeres Design (Beige mit Braun) festgelegt ist, besondere Designs für die drei Schutzumschläge der Tafeln darin.
Es kann also ein Hauptdesign sein, und dann die jeweiligen Ereignisse, die darin eingesetzt werden:
Für Vater, Für Mutter, Danke, Zum Geburtstag, Zum Hochzeitstag
(Immer drei Tafeln, die nebeneinander sichtbar sind)
Es geht nur um die Vorderseite, das Bild kann umlaufend sein wie im Beispiel, muss aber nicht!
Es sind insgesamt 5 verschiedenen Sorten zum machen x 3 Tafeln. Also 15 Variationen.
Für Vater (den besten.., den lieben ... etc.), Für Mutter, Danke, Zum Geburtstag, Zum Hochzeitstag
Alternativ können natürlich auch die jeweiligen Ereignisse extra gemacht werden.
Als Beispiel wie die Schachteln aussehen: In der Anlage Ostern. Das Oster Design ist provisorisch, kann und soll jedoch komplett anders sein. Altersgruppe: Menschen ab 30, die so etwas verschenken
Aufgabenstellung
Alle sollen unterschiedlich sein und einen breiten Verbraucherkreis ansprechen.
Details 4/4-farbig, Material 170 g Bilderdruck glänzend Format 18,8 cm x 15 cm (Achtung: Vorderseite der Tafel
ist nur 18,8 x 7,5 cm, da es ein Schutzumschlag ist.

```html
<!DOCTYPE html>
<html lang="de">
<head>
<meta charset="utf-8">
<title>Silberlund – Schutzumschläge Geschenkbox</title>
<link rel="stylesheet" href="https://fonts.googleapis.com/css2?family=Montserrat:wght@300;500;600;700&family=Great+Vibes&display=swap">
<style>
  :root {
    --bg: #c8c8c8;
    --white: #ffffff;
    --brown: #5a3e33;
    --red: #b11c22;
    --yellow: #e6ac1e;
    --green: #6aa646;
    --magenta: #c4037c;
    --lime: #8ab73e;
    --dark: #222222;
  }
  * { box-sizing: border-box; margin: 0; padding: 0; }
  html, body { width: 1200px; height: 1195px; overflow: hidden; }
  body {
    position: relative;
    background: var(--bg);
    font-family: "Montserrat", Arial, sans-serif;
  }
  .wrapper {
    position: absolute;
    width: 185px;
    height: 462px;
    background: var(--white);
    overflow: hidden;
  }
  .wrapper svg.shapes { position: absolute; inset: 0; width: 100%; height: 100%; }
  .brand {
    position: absolute;
    left: 0; right: 0;
    text-align: center;
    font-weight: 700;
    color: var(--brown);
    letter-spacing: 0.02em;
    font-size: 16px;
    line-height: 1;
  }
  .wrapper--papa .brand { top: 72px; }
  .wrapper--gift .brand { top: 106px; }

  .vertical {
    position: absolute;
    white-space: nowrap;
    transform-origin: left bottom;
    transform: rotate(-90deg);
    line-height: 1;
  }
  .vertical--main { font-weight: 500; font-size: 25px; line-height: 25px; letter-spacing: 0.08em; color: var(--brown); left: 141px; top: 335px; }
  .vertical--sub { font-weight: 300; font-size: 17px; line-height: 17px; letter-spacing: 0.08em; left: 160px; top: 277px; }

  .gift-title {
    position: absolute;
    left: 19px; top: 193px;
    font-weight: 600;
    font-size: 41px;
    line-height: 39px;
    letter-spacing: 0.01em;
  }
  .gift-band { position: absolute; left: 0; right: 0; top: 278px; height: 28px; }
  .gift-field { position: absolute; left: 0; right: 0; top: 306px; bottom: 0; background: var(--dark); }
  .gift-script {
    position: absolute;
    left: 50%; top: 82px;
    transform: translate(-50%, -50%) rotate(-32deg);
    font-family: "Great Vibes", cursive;
    font-size: 40px;
    color: var(--white);
    white-space: nowrap;
  }

  .brand-large {
    position: absolute;
    left: 860px; top: 300px;
    width: 210px;
    text-align: center;
    font-weight: 700;
    font-size: 32px;
    color: var(--brown);
    letter-spacing: 0.02em;
    line-height: 1;
  }
</style>
</head>
<body>

  <section class="wrapper wrapper--papa" style="left:146px; top:125px;">
    <svg class="shapes" viewBox="0 0 287 715" preserveAspectRatio="none" aria-hidden="true">
      <rect x="0" y="0" width="287" height="30" fill="var(--red)"/>
      <rect x="0" y="684" width="287" height="31" fill="var(--brown)"/>
      <rect x="22" y="372" width="20" height="312" fill="var(--brown)"/>
      <rect x="58" y="302" width="20" height="382" fill="var(--red)"/>
      <rect x="94" y="337" width="20" height="347" fill="var(--brown)"/>
      <rect x="130" y="372" width="20" height="312" fill="var(--red)"/>
    </svg>
    <p class="brand">SILBERLUND</p>
    <p class="vertical vertical--main">FÜR PAPA</p>
    <p class="vertical vertical--sub" style="color:var(--red)">DEN LIEBSTEN</p>
  </section>

  <section class="wrapper wrapper--papa" style="left:356px; top:125px;">
    <svg class="shapes" viewBox="0 0 287 715" preserveAspectRatio="none" aria-hidden="true">
      <rect x="0" y="0" width="287" height="30" fill="var(--yellow)"/>
      <rect x="0" y="684" width="287" height="31" fill="var(--brown)"/>
      <g stroke-width="17" stroke-linecap="butt">
        <line x1="-4" y1="450" x2="150" y2="525" stroke="var(--yellow)"/>
        <line x1="-4" y1="492" x2="165" y2="572" stroke="var(--brown)"/>
        <line x1="-4" y1="532" x2="183" y2="622" stroke="var(--yellow)"/>
        <line x1="-4" y1="572" x2="102" y2="622" stroke="var(--brown)"/>
      </g>
    </svg>
    <p class="brand">SILBERLUND</p>
    <p class="vertical vertical--main">FÜR PAPA</p>
    <p class="vertical vertical--sub" style="color:var(--yellow)">DEN COOLSTEN</p>
  </section>

  <section class="wrapper wrapper--papa" style="left:572px; top:125px;">
    <svg class="shapes" viewBox="0 0 287 715" preserveAspectRatio="none" aria-hidden="true">
      <rect x="0" y="0" width="287" height="30" fill="var(--green)"/>
      <rect x="0" y="684" width="287" height="31" fill="var(--brown)"/>
      <rect x="0" y="543" width="123" height="18" fill="var(--brown)"/>
      <rect x="0" y="579" width="151" height="18" fill="var(--green)"/>
      <rect x="0" y="615" width="137" height="18" fill="var(--brown)"/>
      <rect x="0" y="651" width="123" height="18" fill="var(--green)"/>
    </svg>
    <p class="brand">SILBERLUND</p>
    <p class="vertical vertical--main">FÜR PAPA</p>
    <p class="vertical vertical--sub" style="color:var(--green)">DEN TOLLSTEN</p>
  </section>

  <p class="brand-large">SILBERLUND</p>

  <section class="wrapper wrapper--gift" style="left:415px; top:646px;">
    <p class="brand">SILBERLUND</p>
    <h2 class="gift-title" style="color:var(--magenta)">FÜR<br>MAMA</h2>
    <div class="gift-band" style="background:var(--magenta)"></div>
    <div class="gift-field" role="img" aria-label="Dunkles Feld mit magentafarbenen Schokostückchen">
      <p class="gift-script">Die Schönste</p>
    </div>
  </section>

  <section class="wrapper wrapper--gift" style="left:643px; top:646px;">
    <p class="brand">SILBERLUND</p>
    <h2 class="gift-title" style="color:var(--lime)">FÜR<br>MAMA</h2>
    <div class="gift-band" style="background:var(--lime)"></div>
    <div class="gift-field" role="img" aria-label="Dunkles Feld mit grünen Schokostückchen">
      <p class="gift-script">Die Liebste</p>
    </div>
  </section>

  <section class="wrapper wrapper--gift" style="left:877px; top:646px;">
    <p class="brand">SILBERLUND</p>
    <h2 class="gift-title" style="color:var(--yellow)">FÜR<br>PAPA</h2>
    <div class="gift-band" style="background:var(--yellow)"></div>
    <div class="gift-field" role="img" aria-label="Dunkles Feld mit gelben Strichlinien">
      <p class="gift-script">Den Besten</p>
    </div>
  </section>

</body>
</html>
```